JMT - Business Card Design Project

We need a business card based on our logo
Updates

Hi I just upload logo file in AI format Thanks and regards

Target Market(s)

Bank, Big companies, Business owners

Industry/Entity Type

Business

Font styles to use
Sans Serif

```html
<!DOCTYPE html>
<html lang="fr">
<head>
<meta charset="utf-8">
<title>JMT – Business Card</title>
<link href="https://fonts.googleapis.com/css2?family=Questrial&display=swap" rel="stylesheet">
<style>
  :root {
    --page-bg: #e9e7e4;
    --card-white: #ffffff;
    --navy: #13284f;
    --slate: #7d8a8d;
    --text-light: #f4f6f7;
    --text-navy: #1b2f57;
    --tagline: #3a4b6e;
  }
  html, body {
    margin: 0;
    width: 1200px;
    height: 900px;
    overflow: hidden;
    background: var(--page-bg);
    font-family: "Questrial", "Century Gothic", sans-serif;
  }
  .canvas {
    position: relative;
    width: 1200px;
    height: 900px;
    display: flex;
    align-items: center;
    justify-content: center;
  }
  .business-card {
    position: relative;
    width: 840px;
    height: 480px;
    border-radius: 26px;
    overflow: hidden;
    background: var(--card-white);
    box-shadow: 0 10px 30px rgba(0,0,0,0.18);
  }
  .card-bands {
    position: absolute;
    inset: 0;
  }
  .band-navy { fill: var(--navy); }
  .band-slate { fill: var(--slate); }

  .brand {
    position: absolute;
    top: 70px;
    left: 330px;
    color: var(--text-navy);
  }
  .brand-name {
    font-size: 92px;
    line-height: 0.9;
    letter-spacing: 2px;
    margin: 0;
  }
  .brand-company {
    font-size: 21px;
    margin: 6px 0 0;
    letter-spacing: 0.3px;
  }
  .brand-tagline {
    font-size: 11px;
    color: var(--tagline);
    margin: 2px 0 0 18px;
  }

  .holder {
    position: absolute;
    left: 60px;
    top: 368px;
    color: var(--text-light);
  }
  .holder-name {
    font-size: 44px;
    margin: 0;
    letter-spacing: 0.5px;
  }
  .holder-title {
    font-size: 13px;
    margin: 0 0 0 150px;
  }

  .contact-list {
    position: absolute;
    left: 600px;
    top: 238px;
    margin: 0;
    padding: 0;
    list-style: none;
    color: var(--text-light);
    font-size: 15px;
    line-height: 22px;
  }
  .contact-list li {
    display: flex;
    align-items: center;
    gap: 12px;
  }
  .contact-icon {
    width: 11px;
    height: 11px;
    fill: var(--navy);
  }
</style>
</head>
<body>
<main class="canvas">
  <section class="business-card">
    <svg class="card-bands" width="840" height="480" viewBox="0 0 840 480" aria-hidden="true">
      <polygon class="band-slate" points="455,208 840,208 840,480 585,480"/>
      <polygon class="band-navy" points="0,300 405,300 448,232 548,480 0,480"/>
    </svg>

    <header class="brand">
      <h1 class="brand-name">JMT</h1>
      <p class="brand-company">Cabinet Moreau &amp; Associés</p>
      <p class="brand-tagline">Expertise comptable - Audit - Conseil</p>
    </header>

    <div class="holder">
      <p class="holder-name">Paul Martin</p>
      <p class="holder-title">general manager</p>
    </div>

    <ul class="contact-list">
      <li>
        <svg class="contact-icon" viewBox="0 0 12 12" aria-hidden="true"><path d="M2 1h3l1 3-1.5 1a7 7 0 0 0 2.5 2.5L8 6l3 1v3c0 .6-.4 1-1 1A9 9 0 0 1 1 2c0-.6.4-1 1-1z"/></svg>
        <span>001 444 555</span>
      </li>
      <li>
        <svg class="contact-icon" viewBox="0 0 12 12" aria-hidden="true"><path d="M1 3h10v7H1z M1 3l5 4 5-4" /></svg>
        <span>martin@jmt.com</span>
      </li>
      <li>
        <svg class="contact-icon" viewBox="0 0 12 12" aria-hidden="true"><circle cx="6" cy="6" r="5"/></svg>
        <span>www.jmt.com</span>
      </li>
      <li>
        <svg class="contact-icon" viewBox="0 0 12 12" aria-hidden="true"><path d="M6 0a4 4 0 0 1 4 4c0 3-4 8-4 8S2 7 2 4a4 4 0 0 1 4-4z"/></svg>
        <span>adress line.</span>
      </li>
    </ul>
  </section>
</main>
</body>
</html>
```